Martial Arts & Fitness Center Website

We require a wordpress website for a martial arts and fitness company that is located in Stafford, Texas. The name of the facility is Bright Harbor Martial Arts. This company offers various fitness programs throughout the day, after school care with transportation included, and martial arts programs in the evening. Martial Arts programs in the evening is for beginners, intermediate and advanced students. We web design should be clean, crisp, vibrant, and modern. We also require in addition to the standard pages, at a minimum a contact us page, a registration page for various events at the school (lock-ins, parents night out, after school pickup, etc.) once registered we would like the site to have the option to pay for that service as well. We would like to have the ability to include a shopping cart so we can sell gear on the site.

Target Market(s)

Consumers with school age kids, martial artists, parents with kids in martial arts.

Industry/Entity Type

School

Requirements
Must have
• At least a registration page and contact us page. The ability to add more pages later.

School logo is currently being created and the colors is red, white and blue. Will upload logo as soon as it is received.

```html
<!DOCTYPE html>
<html lang="en">
<head>
<meta charset="utf-8">
<title>Bright Harbor Martial Arts</title>
<link href="https://fonts.googleapis.com/css2?family=PT+Sans+Narrow:wght@400;700&family=Quicksand:wght@700&family=Arimo:wght@400;700&display=swap" rel="stylesheet">
<style>
:root{
  --blue-deep:#0a3a6b;
  --blue-mid:#0f5ea8;
  --blue-bright:#1573c4;
  --red:#d3141b;
  --red-dark:#a80b10;
  --ink:#1d1d1d;
  --body-text:#333;
  --page-light:#eceef2;
  --footer:#0c3a68;
  --footer-bottom:#08213c;
  --footer-link:#8fb2d6;
  --white:#fff;
}
*{box-sizing:border-box;margin:0;padding:0}
html,body{width:1052px;height:1200px;overflow:hidden}
body{position:relative;font-family:'Arimo',Arial,sans-serif;color:var(--ink);
  background:linear-gradient(180deg,var(--page-light) 478px,#f8f9fb 760px,#fff 993px)}
.abs{position:absolute}
.header-band{left:0;top:0;width:1052px;height:478px;
  background:linear-gradient(180deg,#0b3768 0%,#0f4f8f 45%,var(--blue-bright) 100%)}
.brand{left:156px;top:32px;color:var(--white);font-family:'PT Sans Narrow',sans-serif;font-weight:700;font-size:27px;line-height:28px;display:flex;align-items:center;gap:8px}
.brand-dot{width:26px;height:26px;border-radius:50%;background:var(--white)}
.search{left:710px;top:12px;width:186px;height:26px;border-radius:13px;background:var(--white);border:2px solid #d9e3ee}
.search span{position:absolute;left:12px;top:5px;font-size:9px;color:#999}
.search b{position:absolute;right:1px;top:1px;height:20px;width:49px;border-radius:10px;background:var(--blue-deep);color:#fff;font-size:9px;font-weight:400;text-align:center;line-height:20px}
.util-links{left:477px;top:70px;font-size:9px;color:var(--white);white-space:nowrap}
.cart-tab{left:778px;top:48px;width:106px;height:50px;border-radius:8px 8px 0 0;background:linear-gradient(180deg,#e8222a,var(--red-dark));color:#fff;font-weight:700;font-size:15px;text-align:center;line-height:48px;transform:skewX(-2deg)}
.nav{left:155px;top:96px;width:740px;height:54px;border-radius:6px;background:linear-gradient(180deg,#1b6cb3,#0c4a86);display:flex;overflow:hidden;box-shadow:0 2px 4px rgba(0,0,0,.3)}
.nav a{display:block;color:#fff;text-decoration:none;font-family:'PT Sans Narrow',sans-serif;font-size:12.5px;line-height:54px;text-align:center;border-right:1px solid #0a3d70;text-transform:uppercase}
.nav a.active{background:linear-gradient(180deg,#e31d24,var(--red-dark))}
.slider-frame{left:184px;top:166px;width:686px;height:315px;background:#ebe8e8;border:1px solid #d6d3d3;box-shadow:0 12px 14px -8px rgba(0,0,0,.3)}
.slider-photo{left:201px;top:182px;width:652px;height:284px;background:linear-gradient(120deg,#c9562a,#d98a45 45%,#f2f2f2 60%,#b8622f)}
.slide-arrow{top:302px;width:30px;height:44px;background:#e9e9e9;border:1px solid #ccc}
.slide-arrow.left{left:155px;border-radius:22px 0 0 22px}
.slide-arrow.right{left:869px;border-radius:0 22px 22px 0}
.section-title{font-family:'Quicksand',sans-serif;font-weight:700;font-size:13px;letter-spacing:1.2px;color:#111}
.intro{left:198px;top:540px;width:454px;font-size:9px;line-height:13.5px;color:var(--body-text)}
.intro strong{display:block;margin-bottom:12px;color:#111}
.video{left:674px;top:529px;width:205px;height:136px;background:#ddd;box-shadow:0 2px 5px rgba(0,0,0,.25)}
.video-still{position:absolute;left:0;top:0;width:205px;height:124px;background:linear-gradient(135deg,#b5a592,#cfc3b4 50%,#a89580)}
.video-bar{position:absolute;left:0;top:124px;width:205px;height:12px;background:#e6e6e6;font-size:4px;color:#888}
.products{left:193px;top:734px;width:666px;height:251px;border-radius:10px;background:var(--blue-mid)}
.card{top:749px;width:156px;height:222px;border-radius:8px;background:#fff;border:1px solid #cfd8e2}
.card-img{position:absolute;left:10px;top:10px;width:134px;height:125px;border-radius:6px;border:1px solid #e2e2e2}
.card-title{position:absolute;left:15px;top:142px;width:130px;font-size:9px;line-height:13.5px;color:#222}
.card-price{position:absolute;left:15px;top:181px;font-family:'PT Sans Narrow',sans-serif;font-size:19px;color:var(--red)}
.card-cart{position:absolute;left:98px;top:174px}
.prod-arrow{top:838px;width:44px;height:44px;border-radius:50%;background:var(--blue-mid)}
.footer{left:0;top:993px;width:1052px;height:175px;background:var(--footer)}
.footer-col{top:1012px;color:var(--white)}
.footer-col h4{font-family:'PT Sans Narrow',sans-serif;font-weight:400;font-size:12px;margin-bottom:7px}
.footer-col a{display:block;font-size:9px;line-height:15.6px;color:var(--footer-link);text-decoration:none}
.currency-label{left:687px;top:1019px;font-size:9px;color:var(--footer-link)}
.currency{left:740px;top:1012px;width:111px;height:25px;border-radius:12px;background:#fff;font-size:9px;color:#555;line-height:25px;padding-left:12px}
.map{left:688px;top:1046px;width:163px;height:107px;border-radius:8px;background:linear-gradient(135deg,#e9e6dd,#d9d5c8);border:2px solid #fff}
.bottom-bar{left:0;top:1168px;width:1052px;height:32px;background:var(--footer-bottom)}
.social{top:1176px;width:15px;height:15px;border-radius:2px;background:#3d6fa8}
.powered{left:264px;top:1178px;font-size:9px;color:#fff}
.pay{top:1177px;width:22px;height:14px;border-radius:2px;background:#e6e6e6}
</style>
</head>
<body>
<div class="abs header-band"></div>

<div class="abs brand"><span class="brand-dot"></span><span>Bright Harbor<br>Martial Arts</span></div>

<div class="abs search"><span>Search the keywords</span><b>Search</b></div>
<div class="abs util-links">Advanced Search &nbsp;|&nbsp; Log In &nbsp;|&nbsp; Create an Account &nbsp;|&nbsp; Shipping &amp; Returns</div>
<div class="abs cart-tab">0 items</div>

<nav class="abs nav">
  <a class="active" style="width:80px">Home</a>
  <a style="width:92px">Courses</a>
  <a style="width:89px">Lock-ins</a>
  <a style="width:152px">Parents Nightout</a>
  <a style="width:119px">School Pickup</a>
  <a style="width:98px">Register</a>
  <a style="width:110px;border-right:0">Contact Us</a>
</nav>

<div class="abs slider-frame"></div>
<div class="abs slider-photo" role="img" aria-label="Children in white uniforms with coloured belts practising punches in a dojo"></div>
<div class="abs slide-arrow left"><svg width="30" height="44"><path d="M19 12 L11 22 L19 32" fill="none" stroke="#999" stroke-width="3"/></svg></div>
<div class="abs slide-arrow right"><svg width="30" height="44"><path d="M10 12 L18 22 L10 32" fill="none" stroke="#999" stroke-width="3"/></svg></div>

<h2 class="abs section-title" style="left:195px;top:511px">WELCOME TO OUR SITE</h2>
<div class="abs intro">
  <strong>Quisque ligula felis, luctus ut posuere vitae, consequat non elit. Morbi at orci dignissim est ornare blandit. Integer eleifend blandit odio, ac rutrum purus auctor ac.</strong>
  Suspendisse augue leo, tempor id consequat et, vestibulum in magna. Suspendisse tincidunt est facilisis velit rutrum dignissim. Integer vestibulum libero ac elit hendrerit malesuada. Nam vulputate vestibulum velit vel elementum. Nam pulvinar suscipit risus eget faucibus. Ut luctus, dolor vel varius ultricies, nunc libero consequat nisi, a bibendum mi risus ultrices augue. Mauris sit amet massa ipsum. Aenean vel tellus eu massa placerat congue. Proin blandit arcu at tortor consectetur nec suscipit ligula dictum. Aliquam justo est, laoreet ac dictum in, vehicula ut dui. Mauris fauci-bus neque id velit eleifend pharetra. Cras lacinia sagittis mi nec hendrerit.
</div>
<div class="abs video">
  <div class="video-still" role="img" aria-label="Video still of two students sparring on a mat"></div>
  <div class="video-bar">
    <svg width="205" height="12"><path d="M6 4 L10 6 L6 8Z" fill="#555"/><rect x="18" y="5" width="102" height="2.5" rx="1" fill="#444"/><rect x="18" y="5" width="50" height="2.5" rx="1" fill="#d3141b"/><circle cx="68" cy="6" r="2.5" fill="#ccc" stroke="#777" stroke-width=".6"/><text x="123" y="8" font-size="4" fill="#888" font-family="Arimo,sans-serif">3:47 / 9:29</text><rect x="160" y="5" width="28" height="2.5" fill="#444"/><rect x="194" y="4" width="4" height="4" fill="#777"/></svg>
  </div>
</div>

<h2 class="abs section-title" style="left:195px;top:703px">FEATURED PRODUCTS</h2>
<div class="abs products"></div>
<div class="abs prod-arrow" style="left:163px"><svg width="44" height="44"><path d="M24 15 L17 22 L24 29" fill="none" stroke="#fff" stroke-width="3.5"/></svg></div>
<div class="abs prod-arrow" style="left:845px"><svg width="44" height="44"><path d="M20 15 L27 22 L20 29" fill="none" stroke="#fff" stroke-width="3.5"/></svg></div>

<div class="abs card" style="left:207px">
  <div class="card-img" role="img" aria-label="Black and blue nunchaku" style="background:linear-gradient(135deg,#fff,#d7e6f3 45%,#3a8fd1 70%,#fff)"></div>
  <div class="card-title">Curabitur elementum turpis a nibh pulvinar vitae ultrices</div>
  <div class="card-price">$19.99</div>
  <svg class="card-cart" width="42" height="34" viewBox="0 0 42 34"><path d="M2 4 H9 L14 22 H34 L38 9 H11" fill="none" stroke="#d3141b" stroke-width="3.5" stroke-linejoin="round"/><path d="M14 15 H36" stroke="#d3141b" stroke-width="3"/><circle cx="16" cy="28" r="3.2" fill="#d3141b"/><circle cx="32" cy="28" r="3.2" fill="#d3141b"/></svg>
</div>
<div class="abs card" style="left:367px">
  <div class="card-img" role="img" aria-label="Blue and black fight shorts" style="background:linear-gradient(135deg,#fff,#1c2a4a 40%,#1e5fb0 70%,#fff)"></div>
  <div class="card-title">Martial Arts Uniforms. MMA fight short</div>
  <div class="card-price">$50.44</div>
  <svg class="card-cart" width="42" height="34" viewBox="0 0 42 34"><path d="M2 4 H9 L14 22 H34 L38 9 H11" fill="none" stroke="#d3141b" stroke-width="3.5" stroke-linejoin="round"/><path d="M14 15 H36" stroke="#d3141b" stroke-width="3"/><circle cx="16" cy="28" r="3.2" fill="#d3141b"/><circle cx="32" cy="28" r="3.2" fill="#d3141b"/></svg>
</div>
<div class="abs card" style="left:528px">
  <div class="card-img" role="img" aria-label="Pair of red boxing gloves" style="background:linear-gradient(135deg,#fff,#e8474a 45%,#c41218 65%,#fff)"></div>
  <div class="card-title">Boxing Gloves Martial Arts Uniforms.</div>
  <div class="card-price">$124.99</div>
  <svg class="card-cart" width="42" height="34" viewBox="0 0 42 34"><path d="M2 4 H9 L14 22 H34 L38 9 H11" fill="none" stroke="#d3141b" stroke-width="3.5" stroke-linejoin="round"/><path d="M14 15 H36" stroke="#d3141b" stroke-width="3"/><circle cx="16" cy="28" r="3.2" fill="#d3141b"/><circle cx="32" cy="28" r="3.2" fill="#d3141b"/></svg>
</div>
<div class="abs card" style="left:688px">
  <div class="card-img" role="img" aria-label="Blue sparring gear set with headguard and pads" style="background:linear-gradient(135deg,#2a3f8f,#fff 45%,#3b4fa0 75%,#fff)"></div>
  <div class="card-title">Martial Arts Uniforms. MMA fight short</div>
  <div class="card-price">$254.99</div>
  <svg class="card-cart" width="42" height="34" viewBox="0 0 42 34"><path d="M2 4 H9 L14 22 H34 L38 9 H11" fill="none" stroke="#d3141b" stroke-width="3.5" stroke-linejoin="round"/><path d="M14 15 H36" stroke="#d3141b" stroke-width="3"/><circle cx="16" cy="28" r="3.2" fill="#d3141b"/><circle cx="32" cy="28" r="3.2" fill="#d3141b"/></svg>
</div>

<footer class="abs footer"></footer>
<div class="abs footer-col" style="left:162px">
  <h4>INFORMATION</h4>
  <a>About Us</a><a>Customer Service</a><a>Site Map</a><a>Search Terms</a><a>Advanced Search</a><a>Orders and Returns</a><a>Contact</a>
</div>
<div class="abs footer-col" style="left:355px">
  <h4>WHY BUY FROM US</h4>
  <a>Shipping &amp; Returns</a><a>Secure Shopping</a><a>International Shipping</a><a>Affiliates</a><a>Group Sales</a>
</div>
<div class="abs footer-col" style="left:548px">
  <h4>MY ACCOUNT</h4>
  <a>Sign In</a><a>View Cart</a><a>My Wishlist</a><a>Track My Order</a><a>Help</a>
</div>
<div class="abs currency-label">Currency:</div>
<div class="abs currency">US Dollars<svg class="abs" style="right:10px;top:9px" width="9" height="7"><path d="M0 0 H9 L4.5 7Z" fill="#1a5fa8"/></svg></div>
<div class="abs map" role="img" aria-label="Street map showing the school location"></div>

<div class="abs bottom-bar"></div>
<div class="abs social" style="left:156px"></div>
<div class="abs social" style="left:178px"></div>
<div class="abs social" style="left:200px;background:#a8332e"></div>
<div class="abs social" style="left:222px"></div>
<div class="abs social" style="left:244px;background:#d9772a"></div>
<div class="abs powered">Powered By Bright Harbor Martial Arts &nbsp;© 2012</div>
<div class="abs pay" style="left:727px"></div>
<div class="abs pay" style="left:754px"></div>
<div class="abs pay" style="left:781px"></div>
<div class="abs pay" style="left:808px"></div>
<div class="abs pay" style="left:835px"></div>
</body>
</html>
```